A resume/portfolio website for myself

I'm an independent software contractor, architect, tech trainer. I need a web site to present myself. Many ready to use portfolio designs are too artistic and focused on presenting design skills of the person. I like a nice website but the content should be a little less graphic than if you would present a graphic designer. Content could be presentation of me, core skill qualities and services and resume. Potentially a page with my tech courses in the longer run

```html
<!DOCTYPE html>
<html lang="en">
<head>
<meta charset="utf-8">
<title>Mark Halden — Software Contractor, Architect, Tech Trainer</title>
<link href="https://fonts.googleapis.com/css2?family=Libre+Baskerville:wght@400;700&family=Mulish:wght@400;600&display=swap" rel="stylesheet">
<style>
:root{
  --ink:#111;
  --night:#0b0b0c;
  --night-2:#1c1f24;
  --paper:#fff;
  --muted:#6d6d72;
  --muted-light:#9a9aa0;
  --accent:#f26a1b;
  --gold:#8b7753;
  --lavender:#d9d9e5;
  --sun:#f0a020;
  --ocean:#1d4a6b;
}
*{margin:0;padding:0;box-sizing:border-box}
html,body{width:1200px;height:4062px;overflow:hidden}
body{background:var(--paper);font-family:'Mulish',sans-serif;color:var(--ink);position:relative}
.serif{font-family:'Libre Baskerville',serif}
section,footer,header{position:absolute;left:0;width:1200px}
.abs{position:absolute}
.photo{position:absolute}

/* hero */
.hero{top:0;height:599px;background:radial-gradient(ellipse at 40% 40%,#24262b 0%,var(--night) 70%)}
.brand{left:96px;top:30px;color:#fff;font-family:'Libre Baskerville',serif;font-size:24px;letter-spacing:.5px}
.burger{left:1066px;top:35px;width:41px}
.burger span{display:block;height:2px;background:#fff;margin-bottom:7px}
.slide-dots{left:43px;top:285px}
.slide-dots i{display:block;width:6px;height:6px;border:1px solid #aaa;border-radius:50%;margin-bottom:4px}
.slide-dots i:first-child{background:#fff;border-color:#fff}
.hero-intro{left:599px;top:238px;color:#fff}
.hero-intro .pre{font-size:28px}
.hero-intro h1{font-size:48px;font-weight:700;letter-spacing:1px;line-height:1.1;border-bottom:1px solid #555;padding-bottom:2px}
.hero-intro .roles{font-size:19px;margin-top:8px}
.scroll-cue{left:1143px;top:302px;color:#aaa;font-size:11px;letter-spacing:3px;writing-mode:vertical-rl;transform:rotate(180deg)}
.scroll-line{left:1154px;top:441px;width:1px;height:134px;background:#444}
.slide-no{left:95px;top:544px;color:#fff;font-family:'Libre Baskerville',serif;font-weight:700;font-size:16px;text-decoration:underline}

/* help */
.help{top:599px;height:473px}
.kicker{font-family:'Libre Baskerville',serif;font-size:17px;text-transform:uppercase}
.title{font-family:'Libre Baskerville',serif;font-weight:700;text-transform:uppercase}
.help .kicker{position:absolute;top:68px;width:100%;text-align:center}
.help .title{position:absolute;top:96px;width:100%;text-align:center;font-size:33px}
.card{position:absolute;top:164px;width:333px;height:215px}
.card .pic{height:175px}
.card .label{height:40px;background:var(--gold);color:#fff;font-family:'Libre Baskerville',serif;font-size:16px;text-align:center;line-height:40px}

/* story */
.story{top:1072px;height:637px;background:linear-gradient(120deg,#2a2d33 0%,var(--night-2) 45%,#0e1013 100%);color:#fff}
.story .kicker{position:absolute;left:93px;top:70px;text-transform:none}
.story .title{position:absolute;left:93px;top:100px;font-size:40px}
.story .lead{position:absolute;left:93px;top:156px;width:510px;font-size:14px;line-height:21px;color:#b5b5bb}
.milestone{position:absolute;left:93px;width:506px;height:83px}
.milestone .year{position:absolute;left:0;width:112px;text-align:right;top:8px;font-size:15px}
.milestone .place{position:absolute;left:0;top:30px;font-size:14px;color:#9a9aa0}
.milestone .dot{position:absolute;left:125px;top:13px;width:7px;height:7px;border-radius:50%;background:var(--accent)}
.milestone h3{position:absolute;left:148px;top:5px;font-family:'Libre Baskerville',serif;font-weight:400;font-size:16px}
.milestone p{position:absolute;left:148px;top:33px;width:360px;font-size:11.5px;line-height:17px;color:#b5b5bb}
.milestone.rule::after{content:"";position:absolute;left:148px;right:0;bottom:0;height:1px;background:#3a3d44}

/* movement */
.movement{top:1709px;height:633px}
.movement .kicker{position:absolute;left:93px;top:62px}
.movement .title{position:absolute;left:93px;top:90px;font-size:35px}
.movement .body{position:absolute;left:93px;width:1014px;font-size:12.5px;line-height:21px;color:var(--muted)}
.movement .ask{position:absolute;left:93px;top:253px;font-family:'Libre Baskerville',serif;font-size:16px}
.points{position:absolute;left:93px;top:293px;list-style:none}
.points li{font-size:12.5px;color:var(--muted);height:37.3px;position:relative;padding-left:13px}
.points li::before{content:"";position:absolute;left:0;top:5px;width:7px;height:7px;border-radius:50%;background:var(--accent)}

/* services */
.services{top:2342px;height:506px;background:linear-gradient(90deg,var(--lavender) 0%,#e8e8ef 50%,var(--lavender) 100%)}
.service{position:absolute;width:330px}
.service .icon{background:var(--ink);border-radius:4px}
.service h3{font-family:'Libre Baskerville',serif;font-weight:400;font-size:25px;margin-top:22px}
.service p{font-size:13px;line-height:20px;color:var(--muted);margin-top:6px}

/* testimonials */
.testimonials{top:2848px;height:503px}
.testimonials .kicker{position:absolute;left:599px;top:130px}
.testimonials .title{position:absolute;left:599px;top:158px;font-size:35px}
.quote{position:absolute;left:599px;top:212px;width:510px;font-size:13px;line-height:20px;color:var(--muted)}
.author{position:absolute;left:599px;top:306px;font-family:'Libre Baskerville',serif;font-size:16px}
.author-role{position:absolute;left:599px;top:327px;font-size:10px;color:var(--muted)}
.pager{position:absolute;left:599px;top:372px}
.pager i{display:inline-block;width:6px;height:6px;background:#444;margin-right:2px}
.pager i:first-child{background:var(--sun)}

/* offer */
.offer{top:3351px;height:363px;background:radial-gradient(ellipse at 70% 50%,#2f6a90 0%,var(--ocean) 45%,#0f2a40 100%);color:#fff}
.offer .pre{position:absolute;left:530px;top:37px;font-family:'Libre Baskerville',serif;font-size:23px}
.offer h2{position:absolute;left:530px;top:70px;font-family:'Libre Baskerville',serif;font-size:33px;font-weight:700}
.form-card{position:absolute;left:530px;top:122px;width:456px;height:206px;background:#fff}
.field{position:absolute;left:30px;width:396px;height:35px;background:#e4e4ea;color:#666;font-size:11px;line-height:35px;padding-left:10px}
.submit{position:absolute;left:30px;top:146px;width:396px;height:35px;background:var(--accent);color:#fff;font-family:'Libre Baskerville',serif;font-size:10px;font-weight:700;text-align:center;line-height:35px;text-transform:uppercase}

/* footer */
.site-footer{top:3714px;height:348px;background:#0a0a0a;color:#fff;text-align:center}
.site-footer .brand-foot{position:absolute;top:78px;width:100%;font-family:'Libre Baskerville',serif;font-size:29px}
.foot-nav{position:absolute;top:119px;width:100%;font-size:12px;color:#ddd}
.foot-nav span{margin:0 7px}
.call{position:absolute;top:158px;width:100%;font-family:'Libre Baskerville',serif;font-size:13px}
.call b{color:var(--accent);font-family:'Mulish',sans-serif;font-weight:400;font-size:14px}
.social{position:absolute;top:201px;left:0;width:100%}
.social i{display:inline-block;width:34px;height:34px;border:1px solid #777;border-radius:50%;margin:0 4px}
.copyright{position:absolute;top:262px;width:100%;font-size:9px;color:#555}
.copyright b{color:#ddd;font-weight:400}
</style>
</head>
<body>

<header class="hero">
  <div class="abs brand">MARK HALDEN</div>
  <div class="abs burger"><span></span><span></span><span></span></div>
  <div class="abs slide-dots"><i></i><i></i><i></i></div>
  <svg class="photo" style="left:173px;top:47px" width="490" height="530" viewBox="0 0 490 530" role="img" aria-label="Portrait of a grey-haired man in a dark suit against a dark organic blob shape">
    <defs><linearGradient id="heroBlob" x1="0" y1="0" x2="1" y2="1"><stop offset="0" stop-color="#2a2c31"/><stop offset="1" stop-color="#050506"/></linearGradient></defs>
    <path d="M120 60 C220 0 360 40 420 150 C480 260 450 380 360 430 C280 475 220 530 120 520 C40 510 10 420 40 330 C70 240 30 120 120 60 Z" fill="url(#heroBlob)"/>
  </svg>
  <div class="abs hero-intro serif">
    <div class="pre">I'm An</div>
    <h1>INDEPENDENT</h1>
    <div class="roles">Software Contractor, Architect Tech Trainer</div>
  </div>
  <div class="abs scroll-cue">SCROLL DOWN</div>
  <div class="abs scroll-line"></div>
  <div class="abs slide-no">01</div>
</header>

<section class="help">
  <div class="kicker">What would you</div>
  <h2 class="title">Like help with today?</h2>
  <div class="card" style="left:93px">
    <div class="pic" role="img" aria-label="Man in a suit standing on a dark background" style="background:linear-gradient(160deg,#25272b,#050505)"></div>
    <div class="label">Software Contractor</div>
  </div>
  <div class="card" style="left:434px">
    <div class="pic" role="img" aria-label="Smiling man in a suit on a light background" style="background:linear-gradient(160deg,#e6e6ee,#c9c9d6)"></div>
    <div class="label">Architect</div>
  </div>
  <div class="card" style="left:773px">
    <div class="pic" role="img" aria-label="Man in a light blue shirt holding a jacket over his shoulder" style="background:linear-gradient(160deg,#e4e4ec,#c4c8d8)"></div>
    <div class="label">Tech Trainer</div>
  </div>
</section>

<section class="story">
  <div class="kicker">History</div>
  <h2 class="title">Our Success Story</h2>
  <p class="lead">If you use this site regularly and would like to help keep the site on the Internet, please consider donating a small sum to help pay for the hosting and bandwidth bill. There is no minimum donation</p>
  <div class="milestone rule" style="top:265px"><span class="year">2000</span><span class="place">Finibus Bonorum</span><span class="dot"></span><h3>These cases are perfectly simple</h3><p>On the other hand, we denounce with righteous indignation and dislike men who are so beguiled and demoralized</p></div>
  <div class="milestone rule" style="top:348px"><span class="year">2008</span><span class="place">Finibus Bonorum</span><span class="dot"></span><h3>These cases are perfectly simple</h3><p>On the other hand, we denounce with righteous indignation and dislike men who are so beguiled and demoralized</p></div>
  <div class="milestone rule" style="top:431px"><span class="year">2015</span><span class="place">Finibus Bonorum</span><span class="dot"></span><h3>These cases are perfectly simple</h3><p>On the other hand, we denounce with righteous indignation and dislike men who are so beguiled and demoralized</p></div>
  <div class="milestone" style="top:514px"><span class="year">2019</span><span class="place">Finibus Bonorum</span><span class="dot"></span><h3>These cases are perfectly simple</h3><p>On the other hand, we denounce with righteous indignation and dislike men who are so beguiled and demoralized</p></div>
  <svg class="photo" style="left:651px;top:63px" width="462" height="512" viewBox="0 0 462 512" role="img" aria-label="Man in a light blue shirt with arms crossed at an office desk, framed in a blob shape">
    <defs><linearGradient id="storyBlob" x1="0" y1="0" x2="1" y2="1"><stop offset="0" stop-color="#1f4663"/><stop offset=".6" stop-color="#16324a"/><stop offset="1" stop-color="#0c1a28"/></linearGradient></defs>
    <path d="M150 20 C230 -20 300 40 330 110 C360 180 470 230 455 350 C440 460 330 520 220 505 C110 490 10 430 5 330 C0 240 90 220 90 140 C90 80 100 45 150 20 Z" fill="url(#storyBlob)"/>
  </svg>
</section>

<section class="movement">
  <div class="kicker">It's time to join</div>
  <h2 class="title">The Movement and Lipsum</h2>
  <p class="body" style="top:151px">On the other hand, we denounce with righteous indignation and dislike men who are so beguiled and demoralized by the charms of pleasure of the moment, so blinded by desire, that they cannot foresee the pain and trouble that are bound to ensue; and equal blame belongs to those who fail in their duty through weakness of will, which is the same as saying through shrinking from toil and pain. These cases are perfectly simple and easy to distinguish. In a free hour, when our power of choice is untrammelled and when nothing prevents our being able to do what we like best, every pleasure is to be welcomed and every pain avoided.</p>
  <p class="ask">Then all of &nbsp;sudden these questions bombard you….</p>
  <ul class="points">
    <li>Vivamus id dui aliquam, cursus sem id, ullamcorper ligula.</li>
    <li>In gravida arcu sed mauris euismod, et pretium velit auctor.</li>
    <li>Cras vestibulum est vitae viverra scelerisque.</li>
    <li>Vivamus id eros bibendum mi volutpat rhoncus eget vitae nisi.</li>
    <li>Nullam blandit nisi efficitur neque egestas congue.</li>
  </ul>
  <p class="body" style="top:492px">On the other hand, we denounce with righteous indignation and dislike men who are so beguiled and demoralized by the charms of pleasure of the moment, so blinded by desire, that they cannot foresee the pain and trouble that are bound to ensue; and equal blame belongs to those who fail in their duty through weakness of will, which is the same as saying through shrinking from toil and pain. These cases are perfectly simple and easy to distinguish. In a free hour, when our power of choice is untrammelled and when nothing prevents our being able to do what we like best, every pleasure is to be welcomed and every pain avoided.</p>
</section>

<section class="services">
  <div class="service" style="left:93px;top:165px">
    <div class="icon" role="img" aria-label="Icon of a computer screen with code and people" style="width:94px;height:74px"></div>
    <h3>Software Contractor</h3>
    <p>If you use this site regularly and would like to help keep the site on the Internet, please consider donating</p>
  </div>
  <div class="photo" role="img" aria-label="Smiling man in a dark suit gesturing with an open hand" style="left:473px;top:-16px;width:300px;height:522px;background:linear-gradient(180deg,#3a3f4c 0%,#1c2230 100%);border-radius:140px 140px 0 0"></div>
  <div class="service" style="left:789px;top:31px">
    <div class="icon" role="img" aria-label="Icon of an architect with a hard hat and blueprint" style="width:90px;height:90px"></div>
    <h3>Architect</h3>
    <p>If you use this site regularly and would like to help keep the site on the Internet, please consider donating</p>
  </div>
  <div class="service" style="left:789px;top:292px">
    <div class="icon" role="img" aria-label="Icon of a trainer presenting a chart to an audience" style="width:72px;height:75px"></div>
    <h3>Tech Trainer</h3>
    <p>If you use this site regularly and would like to help keep the site on the Internet, please consider donating</p>
  </div>
</section>

<section class="testimonials">
  <svg class="photo" style="left:95px;top:60px" width="400" height="380" viewBox="0 0 400 380" role="img" aria-label="Smiling young man with crossed arms in front of a rounded orange shape">
    <rect x="20" y="10" width="360" height="360" rx="60" fill="var(--sun)"/>
  </svg>
  <div class="kicker">Customer</div>
  <h2 class="title">Testimonials</h2>
  <p class="quote">Sed ut perspiciatis unde omnis iste natus error sit voluptatem accusantium doloremque laudantium, totam rem aperiam, eaque ipsa quae ab illo inventore veritatis et quasi architecto beatae vitae dicta sunt explicabo. Nemo enim ipsam voluptatem quia voluptas sit aspernatur aut odit aut fugit…</p>
  <div class="author">Mr. Jhon Doe</div>
  <div class="author-role">Developer</div>
  <div class="pager"><i></i><i></i><i></i></div>
</section>

<section class="offer">
  <div class="photo" role="img" aria-label="Grey-haired man in a suit with arms crossed" style="left:276px;top:0;width:200px;height:363px;background:linear-gradient(180deg,#1b2a38 0%,#101820 100%)"></div>
  <div class="pre">Get your free gift by</div>
  <h2>Completing the form below:</h2>
  <div class="form-card">
    <div class="field" style="top:25px">First Name:</div>
    <div class="field" style="top:64px">Last Name:</div>
    <div class="field" style="top:104px">Email:</div>
    <div class="submit">Get your free quote</div>
  </div>
</section>

<footer class="site-footer">
  <div class="brand-foot">MARK HALDEN</div>
  <nav class="foot-nav"><span>HOME</span>|<span>ABOUT US</span>|<span>PORTFOLIO</span>|<span>CONTACT US</span></nav>
  <div class="call">Call Mark: <b>+2 (555) 240 7300</b></div>
  <div class="social"><i aria-label="Social profile"></i><i aria-label="Social profile"></i><i aria-label="Social profile"></i></div>
  <div class="copyright">COPYRIGHT © 2020 <b>MARK HALDEN</b>. ALL RIGHTS RESERVED</div>
</footer>

</body>
</html>
```